Brochure Design

We need a 6 page Brochure designed for our product, please see attached document for more information. The content should focus on account work.

Target Market(s)

Businesses that use a taxi service for their business

Requirements
Must have
• Must have key content on the services we provide for Account work

```html
<!DOCTYPE html>
<html lang="en">
<head>
<meta charset="utf-8">
<title>Ridelane Business Account Brochure</title>
<link rel="stylesheet" href="https://fonts.googleapis.com/css2?family=Oswald:wght@500;700&family=Lato:wght@400;700&display=swap">
<style>
  :root {
    --page-bg: #dcdcdc;
    --ink-dark: #262626;
    --ink-mid: #3b3b3b;
    --brand-yellow: #f2b53a;
    --brand-yellow-soft: #f7cc72;
    --paper: #ffffff;
    --night-1: #2d1f3a;
    --night-2: #5a3b55;
    --night-glow: #c98b63;
    --body-text: #4a4a4a;
  }
  * { box-sizing: border-box; margin: 0; padding: 0; }
  html, body { width: 880px; height: 1200px; overflow: hidden; background: var(--page-bg); }
  .canvas { position: relative; width: 880px; height: 1200px; }

  .cover { position: absolute; left: 140px; top: 40px; width: 600px; height: 600px; box-shadow: 0 6px 18px rgba(0,0,0,.18); }
  .cover svg { display: block; width: 600px; height: 600px; }

  .spread { position: absolute; left: 20px; top: 720px; width: 840px; height: 280px; background: var(--paper); box-shadow: 0 6px 18px rgba(0,0,0,.18); }
  .spread-art { position: absolute; inset: 0; width: 840px; height: 280px; }

  .headline { font-family: "Oswald", sans-serif; font-weight: 700; text-transform: uppercase; }
  .brand-name { font-family: "Oswald", sans-serif; font-weight: 700; }

  .intro-copy { position: absolute; left: 118px; top: 20px; width: 160px; font-family: "Lato", sans-serif; font-size: 6.6px; line-height: 1.35; color: var(--body-text); }
  .intro-copy p + p { margin-top: 5px; }

  .contact-list { position: absolute; left: 296px; top: 178px; list-style: none; font-family: "Lato", sans-serif; font-size: 8px; color: var(--ink-mid); }
  .contact-list li { display: flex; align-items: center; gap: 5px; margin-bottom: 5px; }
  .contact-icon { width: 10px; height: 10px; flex: none; }

  .site-url { position: absolute; left: 10px; top: 252px; font-family: "Lato", sans-serif; font-size: 7px; color: var(--ink-dark); }
</style>
</head>
<body>
<div class="canvas">

  <section class="cover" aria-label="Brochure front cover">
    <svg viewBox="0 0 600 600" xmlns="http://www.w3.org/2000/svg">
      <defs>
        <linearGradient id="night-photo" x1="0" y1="0" x2="1" y2="1">
          <stop offset="0" stop-color="#7a6a7a"/>
          <stop offset="0.35" stop-color="var(--night-glow)"/>
          <stop offset="0.6" stop-color="var(--night-2)"/>
          <stop offset="1" stop-color="var(--night-1)"/>
        </linearGradient>
        <symbol id="cover-art" viewBox="0 0 600 600">
          <rect class="cover-photo" width="600" height="600" fill="url(#night-photo)" role="img" aria-label="Night photo of a taxi roof sign with blurred city light trails"/>
          <polygon class="cover-dark-band" points="0,230 600,440 600,600 0,600" fill="var(--ink-dark)"/>
          <polygon class="cover-stripe-soft" points="320,300 600,398 600,424 320,326" fill="var(--brand-yellow-soft)" opacity="0.75"/>
          <polygon class="cover-stripe" points="290,338 600,446 600,478 290,370" fill="var(--brand-yellow)"/>
          <polygon class="hex-shadow" points="190,120 305,186 305,320 190,386 75,320 75,186" fill="var(--ink-mid)"/>
          <polygon class="hex-badge" points="175,130 288,195 288,325 175,390 62,325 62,195" fill="var(--brand-yellow)"/>
          <circle cx="104" cy="262" r="12" fill="var(--ink-dark)"/>
          <text class="brand-name" x="124" y="276" font-size="38" fill="var(--ink-dark)">ridelane</text>
          <text class="headline" x="40" y="488" font-size="42" fill="var(--brand-yellow)">Exceptional Travel</text>
          <text class="headline" x="40" y="540" font-size="42" fill="var(--paper)">For a Modern Business</text>
        </symbol>
      </defs>
      <use href="#cover-art" width="600" height="600"/>
    </svg>
  </section>

  <section class="spread" aria-label="Brochure outside spread">
    <svg class="spread-art" viewBox="0 0 840 280" xmlns="http://www.w3.org/2000/svg">
      <defs>
        <linearGradient id="dark-photo" x1="0" y1="0" x2="1" y2="1">
          <stop offset="0" stop-color="#4a4a4a"/>
          <stop offset="1" stop-color="#1e1e1e"/>
        </linearGradient>
        <linearGradient id="app-screens" x1="0" y1="0" x2="1" y2="0">
          <stop offset="0" stop-color="#2a2a2a"/>
          <stop offset="0.5" stop-color="#e8e2c8"/>
          <stop offset="1" stop-color="var(--brand-yellow)"/>
        </linearGradient>
      </defs>
      <!-- back panel -->
      <polygon class="back-yellow" points="0,175 92,120 92,280 0,280" fill="var(--brand-yellow)"/>
      <polygon class="back-dark-tab" points="92,150 104,150 104,280 92,280" fill="var(--ink-dark)"/>
      <rect class="app-screens" x="130" y="176" width="100" height="78" rx="8" fill="url(#app-screens)" role="img" aria-label="Two smartphones showing the booking app map"/>
      <!-- middle panel -->
      <polygon class="mid-stripe-soft" points="420,0 438,0 468,120 450,120" fill="var(--brand-yellow-soft)"/>
      <polygon class="mid-stripe" points="440,0 452,0 482,120 470,120" fill="var(--brand-yellow)"/>
      <polygon class="mid-photo" points="452,0 560,0 560,280 500,280 500,150 482,120" fill="url(#dark-photo)" role="img" aria-label="Dark photo of a passenger seated in an executive car"/>
      <rect class="store-badge" x="418" y="196" width="52" height="17" rx="3" fill="var(--ink-dark)"/>
      <rect class="store-badge" x="418" y="218" width="52" height="17" rx="3" fill="var(--ink-dark)"/>
      <!-- front cover panel -->
      <use href="#cover-art" x="560" y="0" width="280" height="280"/>
    </svg>

    <div class="intro-copy">
      <p>Your business can't wait, but it shouldn't compromise on quality. A Ridelane Business Account guarantees an executive vehicle in London, with 4G Wi-Fi and phone chargers in every vehicle, so you can stay connected to your business every step of your journey.</p>
      <p>Take full control of your business travel with the Ridelane Dispatch Portal, which helps you manage bookings, users, and finances in one space. Plus, with a dedicated account manager, you'll have access to 24/7 support should you need it.</p>
      <p>Open a business account today and take advantage of our executive services outside of London, whether your business travel takes you across Europe, UAE, or Asia.</p>
    </div>

    <ul class="contact-list">
      <li>
        <svg class="contact-icon" viewBox="0 0 10 10"><circle cx="5" cy="5" r="5" fill="var(--brand-yellow)"/><path d="M3.2 2.6l1 .9-.5.8a4 4 0 0 0 2 2l.8-.5.9 1-.7.7C4.8 7.4 2.6 5.2 2.5 3.3z" fill="var(--ink-dark)"/></svg>
        +1(555) 014 2290
      </li>
      <li>
        <svg class="contact-icon" viewBox="0 0 10 10"><circle cx="5" cy="5" r="5" fill="var(--brand-yellow)"/><rect x="2.4" y="3.2" width="5.2" height="3.6" fill="none" stroke="var(--ink-dark)" stroke-width=".8"/><path d="M2.4 3.2L5 5.2l2.6-2" fill="none" stroke="var(--ink-dark)" stroke-width=".8"/></svg>
        hello@ridelane.cab
      </li>
      <li>
        <svg class="contact-icon" viewBox="0 0 10 10"><circle cx="5" cy="5" r="5" fill="var(--brand-yellow)"/><circle cx="5" cy="5" r="2.6" fill="none" stroke="var(--ink-dark)" stroke-width=".7"/><path d="M2.4 5h5.2M5 2.4v5.2" stroke="var(--ink-dark)" stroke-width=".6"/></svg>
        www.ridelane.cab
      </li>
    </ul>

    <div class="site-url">www.ridelane.cab</div>
  </section>

</div>
</body>
</html>
```